Granite Ridge Response Business Card

Side 1: Granite Ridge Response Logo (logo without Maltese cross) with industrial rope rescue related theme. Our company services - TRAINING - Fire Training, Confined Space Rescue Training, Rope Rescue training, Hazmat Training, Incident Command, EMS, Pump Operations Training. Website - graniteridgeresponse.example.
Side 2: Granite Ridge Response Fire Department Logo (logo with Maltese cross) with Firefighter related theme. Company (division) services - FIELD SERVICES - Fire Department, Stand-by Rescue, Safety, EMS, Planning. "Supporting the Emergency Response Community Since 1967"

Add contact information wherever it makes since (Name, Email, Phone).
I would like it to represent the Granite Ridge Response Fire Department Logo as a division not as a separate entity without saying it, possibly by depicting it in the background of Side 2 instead of being a standalone picture like the logo on Side 1.

```html
<!DOCTYPE html>
<html lang="en">
<head>
<meta charset="utf-8">
<title>Granite Ridge Response – Business Cards</title>
<link href="https://fonts.googleapis.com/css2?family=Michroma&family=Saira:wdth,wght@125,400;125,700;125,800&display=swap" rel="stylesheet">
<style>
  :root{
    --backdrop:#2b2b2d;
    --card:#1d1d1f;
    --card-hi:#2c2c2f;
    --red:#e2321f;
    --red-dark:#b8210f;
    --white:#ffffff;
    --grey:#cfcfcf;
    --line:#5a5a5e;
    --fire-1:#ffcf4a;
    --fire-2:#f08a1c;
    --fire-3:#7a2a08;
  }
  *{box-sizing:border-box;margin:0;padding:0}
  html,body{width:1200px;height:1108px;overflow:hidden;background:var(--backdrop)}
  body{font-family:"Saira",sans-serif;font-stretch:125%;color:var(--white);position:relative}

  .card{position:absolute;top:194px;width:420px;height:720px;border-radius:18px;overflow:hidden;
    background:linear-gradient(160deg,var(--card-hi) 0%,var(--card) 55%,#151517 100%)}
  .card--field{left:150px}
  .card--training{left:630px}

  .facet{position:absolute;inset:0;background:rgba(255,255,255,.04);
    clip-path:polygon(100% 0,100% 38%,40% 0)}

  .photo{position:absolute}
  .photo--flames{top:0;right:0;width:420px;height:190px;
    background:radial-gradient(circle at 80% 30%,var(--fire-1),var(--fire-2) 40%,var(--fire-3) 80%);
    clip-path:polygon(30% 0,100% 0,100% 55%)}
  .photo--firefighter{top:330px;left:0;width:420px;height:270px;
    background:radial-gradient(circle at 65% 45%,var(--fire-1),var(--fire-2) 35%,var(--fire-3) 75%,transparent 100%);
    clip-path:polygon(0 0,100% 0,100% 78%,62% 100%,0 100%);opacity:.9}

  .wordmark{position:absolute;left:0;right:0;text-align:center;font-family:"Michroma",sans-serif;
    letter-spacing:.12em;line-height:1.25}
  .card--field .wordmark{top:96px;font-size:28px;color:var(--white)}
  .card--training .wordmark{top:92px;font-size:28px;color:var(--red)}
  .wordmark-rule{position:absolute;left:60px;right:60px;height:2px;background:var(--red)}

  .band{position:absolute;left:0;right:0}
  .band--contact{background:var(--red)}
  .card--field .band--contact{top:212px;height:82px;padding:10px 26px}
  .card--training .band--contact{top:208px;height:110px;padding:12px 26px}

  .phone{display:flex;align-items:center;gap:10px;font-weight:800;font-size:34px;letter-spacing:.02em;line-height:1}
  .phone svg{flex:none}
  .email{font-weight:400;font-size:13.5px;letter-spacing:.06em;text-transform:uppercase;margin-top:6px}
  .person{font-weight:800;font-size:25px;text-transform:uppercase;letter-spacing:.02em;line-height:1.05}
  .role{font-weight:400;font-size:14px;letter-spacing:.12em;text-transform:uppercase;margin-bottom:8px}

  .band--heading{height:46px;background:linear-gradient(90deg,var(--white) 70%,rgba(255,255,255,0));
    color:var(--card);font-weight:800;font-size:28px;letter-spacing:.06em;padding-left:30px;line-height:46px;
    clip-path:polygon(0 0,100% 0,88% 100%,0 100%)}
  .card--field .band--heading{top:294px}
  .card--training .band--heading{top:318px;background:var(--white);clip-path:polygon(0 0,100% 0,100% 40%,80% 100%,0 100%)}

  .services{position:absolute;left:26px;right:26px;list-style:none}
  .card--field .services{top:350px}
  .card--training .services{top:378px}
  .services li{font-weight:700;font-size:15px;letter-spacing:.05em;text-transform:uppercase;
    padding:5px 0 5px;border-bottom:1px solid var(--line)}
  .card--field .services li{padding:4px 0;font-size:15.5px;text-shadow:0 1px 2px rgba(0,0,0,.6)}

  .tagline{position:absolute;top:520px;left:0;right:0;text-align:center;font-weight:700;font-size:15px;
    letter-spacing:.05em;text-transform:uppercase;line-height:1.3}
  .tagline .accent{color:var(--red)}

  .card--training .email--footer{position:absolute;top:618px;left:26px;right:26px;text-align:center;margin:0}

  .band--site{bottom:0;height:78px;background:linear-gradient(90deg,var(--red) 60%,var(--red-dark));
    display:flex;align-items:center;justify-content:center;font-weight:800;font-size:19px;letter-spacing:.03em;
    text-transform:uppercase}
  .card--training .band--site{height:66px}
</style>
</head>
<body>

<article class="card card--field" aria-label="Field services card">
  <div class="facet"></div>
  <div class="photo photo--flames" role="img" aria-label="Photograph of flames"></div>
  <div class="photo photo--firefighter" role="img" aria-label="Photograph of a firefighter working a hose line in front of fire"></div>

  <h1 class="wordmark">GRANITE RIDGE<br>RESPONSE</h1>
  <div class="wordmark-rule" style="top:200px"></div>

  <div class="band band--contact">
    <p class="phone">
      <svg width="30" height="30" viewBox="0 0 30 30" aria-hidden="true"><rect width="30" height="30" rx="6" fill="#fff"/><path d="M9 7c1-1 2.5-1 3 0l1.5 3c.4.8 0 1.6-.6 2l-1 .8c.8 2 2.3 3.6 4.3 4.4l.8-1c.5-.6 1.3-.9 2-.5l3 1.5c1 .5 1 2 0 3-1.5 1.5-3.5 2-5.5 1-4-2-7-5-8.6-9-.8-2-.4-4.4 1.1-5.2z" fill="#e2321f"/></svg>
      555-014-2087
    </p>
    <p class="email">jordan@graniteridgeresponse.example</p>
  </div>

  <h2 class="band band--heading">SERVICES</h2>
  <ul class="services">
    <li>Field Services - Fire Department</li>
    <li>Stand-By Rescue</li>
    <li>Safety</li>
    <li>EMS</li>
    <li>Planning</li>
  </ul>

  <p class="tagline">Supporting the <span class="accent">Emergency</span><br><span class="accent">Response</span> Community<br>Since 1967</p>

  <div class="band band--site">graniteridgeresponse.example</div>
</article>

<article class="card card--training" aria-label="Training card">
  <div class="facet"></div>

  <h1 class="wordmark">GRANITE RIDGE<br>RESPONSE</h1>
  <div class="wordmark-rule" style="top:196px"></div>

  <div class="band band--contact">
    <p class="person">Marcus Delaney</p>
    <p class="role">Managing Director</p>
    <p class="phone">
      <svg width="30" height="30" viewBox="0 0 30 30" aria-hidden="true"><rect width="30" height="30" rx="6" fill="#fff"/><path d="M9 7c1-1 2.5-1 3 0l1.5 3c.4.8 0 1.6-.6 2l-1 .8c.8 2 2.3 3.6 4.3 4.4l.8-1c.5-.6 1.3-.9 2-.5l3 1.5c1 .5 1 2 0 3-1.5 1.5-3.5 2-5.5 1-4-2-7-5-8.6-9-.8-2-.4-4.4 1.1-5.2z" fill="#e2321f"/></svg>
      555-014-2087
    </p>
  </div>

  <h2 class="band band--heading">TRAINING</h2>
  <ul class="services">
    <li>Fire Training</li>
    <li>Confined Space Rescue Training</li>
    <li>Rope Rescue Training</li>
    <li>Hazmat Training</li>
    <li>Incident Command</li>
    <li>EMS</li>
    <li>Pump Operations Training</li>
  </ul>

  <p class="email email--footer">jordan@graniteridgeresponse.example</p>
  <div class="band band--site">graniteridgeresponse.example</div>
</article>

</body>
</html>
```